Outdoor Billboard on PVC (double sides)

Hello, i need special design for billboard which is located 15 meters away from the main road. Measures form Billboard: 8 meters X 2 meters. I need Billboard for Window tinting. I have one picture (white Porsche) which you can use as a main BIG Picture- or you have better idea i am so open to your suggestions. Billboard has to be shocking ... i want to make it look like this is similiar way from style. I have a lot of pictures from my cars which i have done in my garage which we can use it. I dont know if you can use this ... quality? On the billboard so it blames be turn left in 30Meter. My logo wants bi attached- please use it on black background. text which schould be down on the Billboard: Proffesionale Tint my logo VELTANA put somewhere where looks cool Phone: 0664 2915 807 E-mail: marlow.veltana@brisknet.example Website: www. veltana-glasdunkel.at

Target Market(s)

This billboard wants to be on the border between two countrys..i have my garage company here on the border- where ia am making window. A lot of cars are driving each day nearby so I want that people see this and so they look at where they have left to my garage.

Colors

Designer to choose colors to be used in the design.

Requirements
Must have
• Billboard schould have a BiG picture from white Porsche with my logo on the side and text Proffesional scarf tint. Down on the board it schould be info Tel, email, website. This measures 8x2 meters

```html
<!DOCTYPE html>
<html lang="de">
<head>
<meta charset="utf-8">
<title>VELTANA – Billboard Scheibentönung</title>
<link href="https://fonts.googleapis.com/css2?family=Bebas+Neue&family=Nunito:wght@600;700&display=swap" rel="stylesheet">
<style>
  :root {
    --page-bg: #e9eaec;
    --board-dark: #151619;
    --board-mid: #2a2b2f;
    --board-smoke: #4a4c51;
    --accent-red: #e3161e;
    --text-white: #ffffff;
    --text-soft: #e6e6e6;
    --car-light: #f4f5f6;
    --car-shade: #9fa3a8;
  }
  * { box-sizing: border-box; margin: 0; padding: 0; }
  html, body {
    width: 1200px; height: 1200px; overflow: hidden;
    background: var(--page-bg);
  }
  .billboard {
    position: absolute; left: 0; top: 450px;
    width: 1200px; height: 300px; overflow: hidden;
    background:
      radial-gradient(ellipse 420px 170px at 1010px 200px, rgba(120,122,128,.45), transparent 70%),
      linear-gradient(100deg, var(--board-dark) 0%, var(--board-mid) 55%, var(--board-smoke) 100%);
  }
  .hero-car {
    position: absolute; left: 40px; top: 26px;
    width: 590px; height: 196px;
    border-radius: 120px 150px 30px 60px / 90px 100px 30px 40px;
    background: radial-gradient(ellipse at 45% 40%, var(--car-light) 0%, #dfe1e3 45%, var(--car-shade) 100%);
  }
  .brand {
    position: absolute; left: 20px; top: 238px;
    display: flex; align-items: center; gap: 10px;
  }
  .brand-dot {
    width: 32px; height: 32px; border-radius: 50%;
    border: 3px solid var(--accent-red);
  }
  .brand-name {
    font-family: "Bebas Neue", sans-serif;
    font-size: 32px; letter-spacing: 1px; line-height: 1;
    color: var(--accent-red);
  }
  .brand-line {
    position: absolute; left: 172px; top: 253px;
    width: 40px; height: 2px; background: var(--accent-red);
  }
  .decor { position: absolute; left: 0; top: 0; }
  .headline {
    position: absolute; left: 640px; top: 60px;
    font-family: "Bebas Neue", sans-serif;
    font-size: 86px; line-height: .9; letter-spacing: .5px;
    font-weight: 400;
  }
  .headline-red { display: block; color: var(--accent-red); }
  .headline-white { display: block; color: var(--text-white); }
  .contact {
    position: absolute; left: 640px; top: 222px;
    display: flex; align-items: center; gap: 18px;
    font-family: "Nunito", sans-serif; font-weight: 700;
    font-size: 17px; color: var(--text-white);
  }
  .contact-item { display: flex; align-items: center; gap: 6px; }
  .contact-icon {
    width: 15px; height: 15px; border-radius: 3px;
    background: var(--accent-red);
    display: flex; align-items: center; justify-content: center;
  }
  .website {
    position: absolute; left: 640px; top: 256px;
    font-family: "Nunito", sans-serif; font-weight: 600;
    font-size: 15px; letter-spacing: 8.6px; color: var(--text-soft);
  }
</style>
</head>
<body>
  <section class="billboard">
    <svg class="decor" width="1200" height="300" viewBox="0 0 1200 300" aria-hidden="true">
      <line x1="430" y1="246" x2="600" y2="234" stroke="#e3161e" stroke-width="2"/>
      <line x1="600" y1="266" x2="624" y2="210" stroke="#e3161e" stroke-width="2"/>
      <line x1="610" y1="266" x2="634" y2="210" stroke="#e3161e" stroke-width="2"/>
    </svg>

    <div class="hero-car" role="img" aria-label="Large photo of a white sports coupe with tinted windows, three-quarter front view"></div>

    <div class="brand">
      <span class="brand-dot"></span>
      <span class="brand-name">VELTANA</span>
    </div>
    <span class="brand-line"></span>

    <h1 class="headline">
      <span class="headline-red">PROFFESIONELLE</span>
      <span class="headline-white">SCHEIBENTÖNUNG</span>
    </h1>

    <div class="contact">
      <span class="contact-item">
        <span class="contact-icon">
          <svg width="10" height="10" viewBox="0 0 24 24"><path fill="#fff" d="M6.6 10.8a15 15 0 0 0 6.6 6.6l2.2-2.2c.3-.3.7-.4 1-.2 1.1.4 2.3.6 3.6.6.6 0 1 .4 1 1V20c0 .6-.4 1-1 1A17 17 0 0 1 3 4c0-.6.4-1 1-1h3.5c.6 0 1 .4 1 1 0 1.3.2 2.5.6 3.6.1.3 0 .7-.2 1z"/></svg>
        </span>
        0664 2915 807
      </span>
      <span class="contact-item">
        <span class="contact-icon">
          <svg width="10" height="10" viewBox="0 0 24 24"><path fill="none" stroke="#fff" stroke-width="2.5" d="M3 6h18v12H3zM3 6l9 7 9-7"/></svg>
        </span>
        marlow.veltana@brisknet.example
      </span>
    </div>
    <p class="website">www.veltana-glasdunkel.at</p>
  </section>
</body>
</html>
```